Vale Insurance Agency - Business Cards

Hello, I am needing new trendy business cards for our Insurance Agency now that I have a new Logo. I have attached our new logo with several color options along with a business card design that I like. I am leaning towards burgundy and blue colors. I have attached our current business card. I have also attached a headshot of our company president, Dennis Holt, that you can use if you wish. Thank you so much in advance for all the wonderful designs!!!!

Target Market(s)

We want to look very professional to potential customers and we also want to look very professional so insurance companies will want to contract with us to sell their product.

Industry/Entity Type

Insurance

Contact Information for Business Card

Dennis Holt
dholt@valeinsgroup.com
Business: 660-555-0142
Fax: 660-555-0187
Cell: 660-555-0163
Toll Free: 888-555-0119
42 W Elm St Ashford, MO 65010
www.valeinsgroup.net

Font styles to use
Serif
Sans Serif

Colors
0355a3
3277b5
f04a50
ec1f27

Requirements
Nice to have
• I love creativity. The more creative and balanced a business card design the more I will like it. I would like the card to be printed horizontally instead of vertically.
Should not have
• My project should not have the Allied Coverage Broker logo. It is no longer used in the industry.

```html
<!DOCTYPE html>
<html lang="en">
<head>
<meta charset="utf-8">
<title>Vale Insurance Agency – Business Cards</title>
<link rel="stylesheet" href="https://fonts.googleapis.com/css2?family=Montserrat:wght@400;500;700&family=Exo+2:wght@300;400&display=swap">
<style>
  :root {
    --backdrop: #000;
    --burgundy-light: #7c171d;
    --burgundy: #5a0e13;
    --burgundy-dark: #2c0306;
    --gold: #efc31b;
    --cream: #f7efc6;
    --band: #fdf5c9;
    --band-text: #6b1418;
  }
  * { margin: 0; padding: 0; box-sizing: border-box; }
  html, body {
    width: 993px; height: 1200px; overflow: hidden;
    background: var(--backdrop);
  }
  .card {
    position: absolute; left: 31px; width: 912px;
    background: radial-gradient(ellipse 60% 70% at 50% 50%, var(--burgundy-light) 0%, var(--burgundy) 55%, var(--burgundy-dark) 100%);
    overflow: hidden;
  }
  .card--front { top: 43px; height: 520px; }
  .card--back { top: 632px; height: 521px; }

  /* Front */
  .brand-mark {
    position: absolute; left: 83px; top: 188px; width: 148px; height: 148px;
    border: 12px solid var(--gold); border-radius: 50%;
  }
  .brand-divider {
    position: absolute; left: 297px; top: 173px; width: 3px; height: 177px;
    background: var(--gold);
  }
  .brand-name {
    position: absolute; left: 324px; top: 215px; width: 505px;
    font-family: "Montserrat", sans-serif; font-weight: 700; color: var(--gold);
  }
  .brand-name__main { display: block; font-size: 52px; line-height: 58px; letter-spacing: 0.3px; white-space: nowrap; }
  .brand-name__sub {
    display: flex; align-items: center; gap: 10px; margin-top: -4px;
    font-size: 32px; line-height: 40px; letter-spacing: 8px; white-space: nowrap;
  }
  .brand-name__sub::before, .brand-name__sub::after {
    content: ""; flex: 1; height: 3px; background: var(--gold);
  }

  /* Back */
  .person { position: absolute; left: 31px; top: 34px; width: 340px; }
  .person__name {
    font-family: "Montserrat", sans-serif; font-size: 43px; color: var(--cream);
    white-space: nowrap; line-height: 50px;
  }
  .person__name strong { font-weight: 700; }
  .person__name span { font-weight: 400; }
  .person__title {
    display: flex; align-items: center; gap: 12px; width: 268px; margin: 2px 0 0 27px;
    font-family: "Montserrat", sans-serif; font-weight: 500; font-size: 30px; line-height: 36px; color: var(--gold);
  }
  .person__title::before, .person__title::after { content: ""; flex: 1; height: 3px; background: var(--gold); }

  .contact { position: absolute; left: 31px; font-family: "Exo 2", sans-serif; font-weight: 300; font-size: 20.5px; color: var(--cream); }
  .contact__icon { position: absolute; left: 0; top: -2px; width: 29px; height: 29px; }
  .contact__text { margin-left: 38px; line-height: 26.3px; white-space: nowrap; }
  .contact--email { top: 165px; }
  .contact--phone { top: 220px; }
  .contact--address { top: 354px; }

  .back-mark {
    position: absolute; left: 513px; top: 100px; width: 270px; height: 270px;
    border: 17px solid var(--gold); border-radius: 50%;
  }
  .back-mark-name {
    position: absolute; left: 448px; top: 392px; width: 400px; text-align: center;
    font-family: "Montserrat", sans-serif; font-weight: 700; font-size: 24px; color: var(--gold);
    letter-spacing: 1px; white-space: nowrap;
  }

  .web-band {
    position: absolute; left: 0; bottom: 0; width: 100%; height: 44px;
    background: var(--band); text-align: center;
    font-family: "Exo 2", sans-serif; font-size: 19px; line-height: 44px; color: var(--band-text);
  }
</style>
</head>
<body>
  <section class="card card--front">
    <div class="brand-mark"></div>
    <div class="brand-divider"></div>
    <div class="brand-name">
      <span class="brand-name__main">VALE INSURANCE</span>
      <span class="brand-name__sub">AGENCY INC</span>
    </div>
  </section>

  <section class="card card--back">
    <div class="person">
      <h1 class="person__name"><strong>DENNIS</strong> <span>HOLT</span></h1>
      <p class="person__title">CEO</p>
    </div>

    <div class="contact contact--email">
      <svg class="contact__icon" viewBox="0 0 29 29" aria-hidden="true">
        <circle cx="14.5" cy="14.5" r="14.5" fill="var(--gold)"/>
        <rect x="7.5" y="9.5" width="14" height="10" fill="none" stroke="var(--burgundy)" stroke-width="1.6"/>
        <path d="M7.5 9.5 L14.5 15 L21.5 9.5 M7.5 19.5 L12.5 14.5 M21.5 19.5 L16.5 14.5" fill="none" stroke="var(--burgundy)" stroke-width="1.4"/>
      </svg>
      <p class="contact__text">dholt@valeinsgroup.com</p>
    </div>

    <div class="contact contact--phone">
      <svg class="contact__icon" viewBox="0 0 29 29" aria-hidden="true">
        <circle cx="14.5" cy="14.5" r="14.5" fill="var(--gold)"/>
        <path d="M6 14 Q14.5 8 23 14 L21 17 L18 15.5 L18 13.5 Q14.5 12 11 13.5 L11 15.5 L8 17 Z" fill="var(--burgundy)"/>
      </svg>
      <p class="contact__text">Business: 660-555-0142<br>Fax: 660-555-0187<br>Cell: 660-555-0163<br>Toll Free: 888-555-0119</p>
    </div>

    <div class="contact contact--address">
      <svg class="contact__icon" viewBox="0 0 29 29" aria-hidden="true">
        <circle cx="14.5" cy="14.5" r="14.5" fill="var(--gold)"/>
        <path d="M14.5 5.5 a6 6 0 0 1 6 6 c0 4.5 -6 11.5 -6 11.5 s-6 -7 -6 -11.5 a6 6 0 0 1 6 -6 z" fill="var(--burgundy)"/>
        <circle cx="14.5" cy="11.5" r="2.4" fill="var(--gold)"/>
      </svg>
      <p class="contact__text">42 W Elm St Ashford, MO 65010</p>
    </div>

    <div class="back-mark"></div>
    <p class="back-mark-name">VALE INSURANCE AGENCY</p>

    <footer class="web-band">www.valeinsgroup.net</footer>
  </section>
</body>
</html>
```